Luma Harbor Vow Studio, Inc.

Luma Harbor Vow Studio Business Card design for Cardlyne. Clean, contemporary, creative, colorful (using colors provided). ONE SIDE SHOULD INCLUDE logo, www.lumaharborvowstudio.com, @sayidoatluma. OTHER SIDE SHOULD INCLUDE Delia Brennan. Owner & Officiant. Calder Cove, Port Linden. 555.014.2871. delia@lumaharborvowstudio.com. Colors are blue #58AA9E
and golden #e2bf80)

Target Market(s)

Destination Wedding Clients in the United States

Contact Information for Business Card

Delia Brennan
Owner & Officiant
Calder Cove, Port Linden
555.014.2871
delia@lumaharborvowstudio.com

Font styles to use
Sans Serif

Requirements
Must have
• Colorful (colors are blue #58AA9E
• and golden #e2bf80), clean, contemporary. ONE SIDE SHOULD INCLUDE logo, www.lumaharborvowstudio.com, @sayidoatluma. Other side should include Delia Brennan. Owner & Officiant. Calder Cove, Port Linden. 555.014.2871. delia@lumaharborvowstudio.com
Nice to have
• I would like to see a version that includes my bio photo, and one that doesn't include the bio photo

```html
<!DOCTYPE html>
<html lang="en">
<head>
<meta charset="utf-8">
<title>Luma Harbor Vow Studio – Business Card</title>
<link rel="stylesheet" href="https://fonts.googleapis.com/css2?family=Open+Sans:wght@400&family=Great+Vibes&display=swap">
<style>
  :root {
    --backdrop: #1c1815;
    --gold-light: #dcc08a;
    --gold-mid: #b49a66;
    --gold-dark: #8e7a4f;
    --tan: #c99a6c;
    --tan-dark: #b5845a;
    --cream: #fbf1e6;
    --frame-line: #f6e7d6;
    --ink: #1e1a17;
    --white: #ffffff;
  }
  * { margin: 0; padding: 0; box-sizing: border-box; }
  html, body {
    width: 1200px; height: 1200px; overflow: hidden;
    background: var(--backdrop);
  }
  .sheet {
    position: relative; width: 1200px; height: 1200px;
  }
  .card {
    position: absolute; left: 250px; width: 700px; height: 400px;
    overflow: hidden; border-radius: 3px;
  }
  .card--front {
    top: 150px;
    background: radial-gradient(ellipse at 45% 30%, var(--gold-light) 0%, var(--gold-mid) 45%, var(--gold-dark) 100%);
    color: var(--white);
    display: flex; flex-direction: column; align-items: center; justify-content: center;
  }
  .brand {
    display: flex; align-items: center; gap: 14px;
    font-family: "Open Sans", sans-serif; font-weight: 400;
    font-size: 34px; letter-spacing: 2px; color: var(--white);
  }
  .brand__dot {
    width: 22px; height: 22px; border-radius: 50%; background: var(--white);
  }
  .front__links {
    margin-top: 48px;
    font-family: "Open Sans", sans-serif; font-size: 17px; color: var(--white);
    letter-spacing: .3px;
  }
  .card--back { top: 650px; }
  .portrait {
    position: absolute; inset: 0;
    background: radial-gradient(ellipse at 55% 50%, #d9b38a 0%, var(--tan) 50%, var(--tan-dark) 100%);
  }
  .frame {
    position: absolute; left: 140px; top: 80px; width: 420px; height: 250px;
    border: 5px solid var(--frame-line);
    padding: 10px;
  }
  .frame__panel {
    width: 100%; height: 100%;
    background: rgba(251, 241, 230, 0.82);
    display: flex; flex-direction: column; align-items: center; justify-content: center;
    font-family: "Open Sans", sans-serif; color: var(--ink); text-align: center;
  }
  .contact__name {
    font-family: "Great Vibes", cursive; font-size: 44px; line-height: 1; margin-bottom: 4px;
  }
  .contact__title { font-size: 14px; margin-bottom: 16px; }
  .contact__line { font-size: 14px; line-height: 1.55; }
</style>
</head>
<body>
<main class="sheet">
  <section class="card card--front">
    <div class="brand"><span class="brand__dot"></span>Luma Harbor Vow Studio</div>
    <p class="front__links">www.lumaharborvowstudio.com | @sayidoatluma.</p>
  </section>

  <section class="card card--back">
    <div class="portrait" role="img" aria-label="Bio photo of the owner and officiant"></div>
    <div class="frame">
      <div class="frame__panel">
        <p class="contact__name">Delia Brennan</p>
        <p class="contact__title">Owner &amp; Officiant</p>
        <p class="contact__line">555.014.2871</p>
        <p class="contact__line">Calder Cove, Port Linden</p>
        <p class="contact__line">delia@lumaharborvowstudio.com</p>
      </div>
    </div>
  </section>
</main>
</body>
</html>
```